Small IT consulting firm needs a new web site

Quillmark Solutions, LLC is a company based out of Arizona with national presence. We work on both national, multinational, and international projects. We are Brindlesoft Partners. Heavy experience and work with Orbitline Control Kit, Vantra, Deskhub 720 . We offer Architecture, Design, Development, and implementation services. We have a specialty in Deskhub 720 migrations and implementations. We also have a specialized practice in Program and Project Management. The design message should foster a feeling of partnership and experience. Attached is my logo.

```html
<!DOCTYPE html>
<html lang="en">
<head>
<meta charset="utf-8">
<title>Quillmark Solutions, LLC – About</title>
<link rel="stylesheet" href="https://fonts.googleapis.com/css2?family=Michroma&family=Didact+Gothic&display=swap">
<style>
  :root {
    --brand-red: #cc1c2a;
    --steel-gray: #767676;
    --heading-gray: #5a5a5a;
    --text-gray: #555555;
    --panel-gray: #ebebeb;
    --button-gray: #d3d3d3;
    --white: #ffffff;
  }
  * { margin: 0; padding: 0; box-sizing: border-box; }
  html, body { width: 1106px; height: 1200px; overflow: hidden; background: var(--white); }
  .page { position: relative; width: 1106px; height: 1200px; overflow: hidden; font-family: "Didact Gothic", sans-serif; color: var(--text-gray); }
  .backdrop { position: absolute; inset: 0; }

  .brand { position: absolute; left: 158px; top: 120px; display: flex; align-items: center; gap: 10px; }
  .brand-mark { width: 34px; height: 34px; background: var(--brand-red); }
  .brand-name { font-family: "Michroma", sans-serif; font-size: 13px; color: var(--brand-red); line-height: 1.35; }

  .main-nav { position: absolute; top: 54px; right: 159px; display: flex; gap: 22px; }
  .main-nav a { font-family: "Michroma", sans-serif; font-size: 12px; color: var(--steel-gray); text-decoration: none; height: 33px; line-height: 33px; padding: 0 3px; letter-spacing: 0.5px; }
  .main-nav a.is-active { background: var(--brand-red); color: var(--white); padding: 0 13px; }

  .hero-visual { position: absolute; left: 240px; top: 254px; width: 205px; height: 196px; background: radial-gradient(ellipse at 55% 45%, #f2f2f2 0%, #cfcfcf 60%, #ffffff 100%); }
  .hero-copy { position: absolute; left: 543px; top: 268px; width: 370px; }
  .hero-title { font-family: "Michroma", sans-serif; font-size: 26px; line-height: 31px; color: var(--steel-gray); font-weight: 400; }
  .hero-title .accent { color: var(--brand-red); display: block; }
  .hero-text { font-family: Arial, sans-serif; font-size: 10px; line-height: 12px; color: #8a8a8a; margin: 7px 0 0 5px; width: 360px; }
  .button { display: inline-block; margin: 13px 0 0 3px; width: 118px; height: 30px; line-height: 30px; text-align: center; background: var(--button-gray); color: var(--steel-gray); font-family: "Michroma", sans-serif; font-size: 9px; text-decoration: none; }

  .services { position: absolute; left: 160px; top: 478px; width: 790px; }
  .section-title { font-family: "Michroma", sans-serif; font-weight: 400; font-size: 21px; color: var(--brand-red); letter-spacing: 1px; }
  .services p { font-size: 13px; line-height: 15.3px; margin-top: 15px; }
  .services p:first-of-type { margin-top: 30px; }

  .expertise-title { position: absolute; right: 159px; top: 858px; font-family: "Michroma", sans-serif; font-weight: 400; font-size: 21px; color: var(--heading-gray); letter-spacing: 1px; }
  .partner-row { position: absolute; top: 950px; left: 220px; width: 680px; display: flex; justify-content: space-between; align-items: center; }
  .partner { display: flex; align-items: center; gap: 8px; font-size: 22px; color: #222; }
  .partner-mark { width: 22px; height: 22px; background: var(--steel-gray); }
  .expertise-text { position: absolute; left: 161px; top: 1052px; width: 780px; font-size: 13px; line-height: 15.3px; }

  .site-footer { position: absolute; left: 0; top: 1165px; width: 1106px; height: 35px; background: var(--panel-gray); text-align: center; font-family: Arial, sans-serif; font-size: 8.5px; line-height: 35px; color: #666; }
</style>
</head>
<body>
<div class="page">
  <svg class="backdrop" width="1106" height="1200" viewBox="0 0 1106 1200" aria-hidden="true">
    <polygon points="0,184 158,248 1106,132 1106,176 158,258 0,196" fill="var(--brand-red)"/>
    <polygon points="0,176 158,244 1106,112 1106,136 158,250 0,186" fill="var(--steel-gray)"/>
    <polygon points="0,450 1106,450 1106,778 946,714 0,796" fill="var(--panel-gray)"/>
    <polygon points="0,796 946,714 1106,778 1106,790 946,722 0,836" fill="var(--brand-red)"/>
    <polygon points="0,836 946,722 1106,790 1106,800 946,728 0,862" fill="var(--steel-gray)"/>
  </svg>

  <header>
    <div class="brand">
      <span class="brand-mark"></span>
      <span class="brand-name">Quillmark<br>Solutions, LLC</span>
    </div>
    <nav class="main-nav">
      <a href="#">HOME</a>
      <a href="#" class="is-active">ABOUT</a>
      <a href="#">SERVICES</a>
      <a href="#">CONTACT US</a>
    </nav>
  </header>

  <div class="hero-visual" role="img" aria-label="Illustration of a white robot head in profile"></div>
  <section class="hero-copy">
    <h1 class="hero-title">WE'RE COMMITED <span class="accent">TO YOUR SUCCESS</span></h1>
    <p class="hero-text">Lorem ipsum dolor sit amet, consectetur adipiscing elit, sed do eiusmod tempor incididunt ut labore et dolore magna aliqua. Ut enim ad minim veniam, quis nostrud exercitation ullamco laboris nisi ut aliquip ex ea commodo consequat.</p>
    <a class="button" href="#">CONTACT US</a>
  </section>

  <section class="services">
    <h2 class="section-title">QUILLMARK SOLUTIONS, LLC SERVICES</h2>
    <p>At Quillmark Solutions, LLC, we take care to provide our customers high quality services personalized for the unique needs.<br>We are available to take your requests for further information 24 hours a day, 7 days a week. Our staff members are professional, courteous and efficient, and we will respond to you within 24 hours of your submission.</p>
    <p>If you have any initiatives that you would like some assistance with, please don't hesitate to reach out to us.<br>We will be happy to discuss your initiatives with you with no obligations, or commitments, required. Once you have had<br>your initial conversations</p>
  </section>

  <h2 class="expertise-title">WE ARE HEAVILY EXPERIENCED IN</h2>
  <div class="partner-row">
    <div class="partner"><span class="partner-mark"></span>Orbitline Control Kit</div>
    <div class="partner"><span class="partner-mark"></span>Brindlesoft Vantra</div>
    <div class="partner"><span class="partner-mark"></span>Deskhub 720</div>
  </div>
  <p class="expertise-text">We work on both national, multinational, and international projects. We are Brindlesoft Partners. Heavy experience and work with Orbitline Control Kit, Vantra, Deskhub 720 . We offer Architecture, Design, Development, and implementation services. We have a specialty in Deskhub 720 migrations and implementations. We also have a specialized practice in Program and Project Management.</p>

  <footer class="site-footer">Copyright © 2015 Quillmark Solutions, LLC. Use of this website constitutes acceptance of our User Agreement and Privacy Policy.</footer>
</div>
</body>
</html>
```